Brand New Winery Label. You could help launch an entire winery with this label design.

Create a unique and compelling Wine Label. I am looking for a distinctive wine label that features an old wood picnic table with two old chairs and a wine bottle sitting on that table. It should be a hand drawing, sort of like pen and ink or charcoal type feeling; not a photograph and not computer cut and paste images! The old wood table is in the shade of, and directly under an old, gnarled olive tree. There are no people, just an inviting rustic picnic table with the two old chairs and the ancient olive tree overhead. The entire image must work well on a wine label, that measures roughly 3.5 inches across and about 4 inches tall, so it cannot be overly intricate or too small. if you need more from me, simply let me know and I will try and help you with other ideas.
Updates

I’m on a business trip and only have access to Zelfon until the weekend. I want to carefully review any submission on a proper screen and provide feedback.

Target Market(s)

Wine stores, liquor stores, grocery store shelves, website, etc.

Industry/Entity Type

Winery

Font styles to use
Serif

Colors
000000
474747
d3d3d3
151515
cadf82
fee18a
b8a5cd

Requirements
Must have
• See attached photos for inspiration, especially about the Olive trees and how I want to have the table and chairs surrounded by the trees. Old wood picnic table, slightly beat up and sort of falling apart. Old, but loved. A bottle of white wine on the table and only TWO old wood French Bistro chairs next to the table. Must have an old gnarled olive tree next to the table and the table would be in the shade of that tree. You feel ensconced in lush, shady Olive trees It should look like a hand drawing, maybe charcoal type or pen and ink or marking pen type look. I'm thinking black and white, but I am definitely open to colors.
• Label should say: Las Brumas Wines 2017 Chardonnay Santa Rita Hills AVA
• Please see the photos I attached to the project brief. The idea is that the table is under the canopy of the olive trees so that the whole thing feels like you are in an Olive Grove, lavendar in the foreground and no bricks, no house, no other structures. you are just out in a big Olive Orchard
Nice to have
• The label size is roughly 3.5 inches wide and 4 inches tall. The image will be horizontal. It should be a crisp image, sort of like an illustration, definitely not a painting. Please let me know if you have any more questions!
Should not have
• no computer generated graphics. No cut and paste images. It should NOT be a photograph or photo realistic

```html
<!DOCTYPE html>
<html lang="en">
<head>
<meta charset="utf-8">
<title>Las Brumas Vines — Chardonnay Label</title>
<link rel="stylesheet" href="https://fonts.googleapis.com/css2?family=Rye&family=Playfair+Display:ital,wght@0,400;0,700;1,400&display=swap">
<style>
  :root {
    --backdrop: #383830;
    --paper: #f1ece0;
    --rust: #a8693d;
    --ink: #151515;
    --sketch: #8e8e8a;
    --sketch-light: #c9c9c4;
  }
  * { margin: 0; padding: 0; box-sizing: border-box; }
  html, body {
    width: 1200px;
    height: 1018px;
    overflow: hidden;
    background: var(--backdrop);
  }
  .label {
    position: absolute;
    left: 270px;
    top: 128px;
    width: 655px;
    height: 749px;
    background: var(--paper);
    font-family: "Playfair Display", Georgia, serif;
    text-align: center;
  }
  .label__illustration {
    position: absolute;
    left: 184px;
    top: 68px;
    width: 280px;
    height: 248px;
    border-radius: 46% 46% 8% 8% / 40% 40% 8% 8%;
    background: radial-gradient(ellipse at 50% 40%, #a9a9a5 0%, #bcbcb7 45%, rgba(241,236,224,0) 75%);
  }
  .label__title {
    position: absolute;
    left: 0;
    top: 0;
    width: 655px;
    height: 749px;
  }
  .label__title text {
    font-family: "Rye", Georgia, serif;
    font-size: 84px;
    fill: var(--rust);
  }
  .label__subline {
    position: absolute;
    left: 0;
    top: 446px;
    width: 655px;
    height: 44px;
  }
  .flourish {
    position: absolute;
    top: 14px;
    width: 130px;
    height: 16px;
    border-radius: 50%;
  }
  .flourish--left {
    left: 86px;
    background: linear-gradient(90deg, rgba(142,142,138,0) 0%, var(--sketch-light) 45%, var(--sketch) 100%);
  }
  .flourish--right {
    right: 84px;
    background: linear-gradient(270deg, rgba(142,142,138,0) 0%, var(--sketch-light) 45%, var(--sketch) 100%);
  }
  .label__vines {
    position: absolute;
    left: 0;
    width: 655px;
    top: 0;
    font-weight: 700;
    font-size: 42px;
    line-height: 44px;
    letter-spacing: 20px;
    padding-left: 20px;
    color: var(--ink);
  }
  .label__varietal {
    position: absolute;
    left: 0;
    width: 655px;
    top: 534px;
    font-size: 31px;
    line-height: 36px;
    letter-spacing: 10px;
    padding-left: 10px;
    color: var(--rust);
    font-weight: 700;
  }
  .label__region {
    position: absolute;
    left: 0;
    width: 655px;
    top: 580px;
    font-size: 22px;
    line-height: 28px;
    letter-spacing: 5.5px;
    padding-left: 5px;
    color: var(--rust);
  }
  .label__vintage {
    position: absolute;
    left: 0;
    width: 655px;
    top: 630px;
    font-size: 25px;
    line-height: 30px;
    font-style: italic;
    letter-spacing: 7px;
    padding-left: 7px;
    color: var(--ink);
  }
  .label__base-flourish {
    position: absolute;
    left: 262px;
    top: 680px;
    width: 112px;
    height: 16px;
    border-radius: 50%;
    background: linear-gradient(90deg, rgba(142,142,138,0) 0%, var(--sketch-light) 50%, rgba(142,142,138,0) 100%);
  }
</style>
</head>
<body>
  <main class="label">
    <div class="label__illustration" role="img" aria-label="Pen-and-ink drawing of a gnarled olive tree shading a rustic wooden table with a wine bottle and two bistro chairs"></div>

    <svg class="label__title" viewBox="0 0 655 749" aria-label="Las Brumas">
      <defs>
        <path id="title-arc" d="M 106 436 Q 322 392 538 436"/>
      </defs>
      <text><textPath href="#title-arc" textLength="432" lengthAdjust="spacingAndGlyphs">LAS BRUMAS</textPath></text>
    </svg>

    <div class="label__subline">
      <div class="flourish flourish--left" role="img" aria-label="Decorative scroll flourish"></div>
      <div class="label__vines">VINES</div>
      <div class="flourish flourish--right" role="img" aria-label="Decorative scroll flourish"></div>
    </div>

    <div class="label__varietal">CHARDONNAY</div>
    <div class="label__region">SANTA RITA HILLS AVA</div>
    <div class="label__vintage">2017</div>
    <div class="label__base-flourish" role="img" aria-label="Decorative scroll flourish"></div>
  </main>
</body>
</html>
```